Brenwick Structures Construction Company Seeking Modern Website

We are a small construction company wanting to create a web presence. We don't have much in the way of current content but will get photos as they come in. Attached is a picture of our business card.
The pages we would like on the menu are:
Home
Portfolio
Product Specs
Testimonials
Our Process
Contact
Some designs we like are:
http://www.tovandrafters.example/
http://www.qrkframes.example/
http://harnestshed.example/
http://pellowbarns.example/
Not much requirements other than that so feel free to be creative!
Target Market(s)
Construction
Commercial and Residential Buildings
Industry/Entity Type
Construction Company
Number of Pages Required
5+ page

```html
<!DOCTYPE html>
<html lang="en">
<head>
<meta charset="utf-8">
<title>Brenwick Structures — Home</title>
<link href="https://fonts.googleapis.com/css2?family=Lato:ital,wght@0,400;0,700;1,400&family=Roboto:wght@500&display=swap" rel="stylesheet">
<style>
:root{
  --blue:#1a9ad6;
  --red:#d9261c;
  --text:#555;
  --dark:#333;
  --grey-band:#ececec;
  --footer:#2e2e2e;
  --line:#e2e2e2;
}
*{box-sizing:border-box;margin:0;padding:0}
html,body{width:882px;height:1200px;overflow:hidden;background:#fff}
body{position:relative;font-family:"Lato",sans-serif;color:var(--text)}
.abs{position:absolute}
.top-bar{left:0;top:0;width:882px;height:3px;background:var(--blue)}
.brand{left:96px;top:26px;display:flex;align-items:center;gap:8px;font-size:24px;font-weight:700;color:var(--red)}
.brand-dot{width:14px;height:14px;border-radius:50%;background:var(--blue)}
.call{right:98px;top:31px;font-size:15px;display:flex;align-items:center;gap:10px}
.call em{color:#666}
.call .phone{color:var(--blue);font-weight:700;display:flex;align-items:center;gap:5px;font-size:13.5px}
.nav{left:0;top:78px;width:882px;height:34px;border-top:1px solid var(--line);border-bottom:1px solid var(--line)}
.nav ul{list-style:none;position:absolute;left:96px;top:7px;display:flex}
.nav li{width:115px;text-align:center;font-size:11px;line-height:19px;color:#777;border-left:1px solid var(--line)}
.nav li:last-child{border-right:1px solid var(--line)}
.nav li.active{color:var(--red)}
.hero{left:0;top:112px}
.hero-title{left:0;top:232px;width:882px;text-align:center;font-size:28px;color:#fff;text-shadow:0 2px 4px rgba(0,0,0,.45)}
.welcome{left:0;top:478px;width:882px;text-align:center;font-size:22px;color:#777}
.welcome span{color:var(--blue)}
.intro{left:108px;top:519px;width:666px;text-align:center;font-size:11.3px;line-height:15.6px;color:#666}
.read-more{left:0;top:584px;width:882px;text-align:center;font-size:11px;font-weight:700;color:var(--blue)}
.card{top:638px;width:213px;height:222px;border:1px solid #e4e4e4;border-top:2px solid var(--blue);background:#fff;box-shadow:0 8px 8px -6px rgba(0,0,0,.15)}
.card-head{position:absolute;left:10px;top:10px;display:flex;align-items:center;gap:8px;font-size:14.5px;color:var(--blue)}
.icon{width:27px;height:27px;border-radius:50%;background:var(--red);display:flex;align-items:center;justify-content:center}
.news-item{position:absolute;left:10px;width:190px;display:flex;gap:8px;padding-bottom:5px;border-bottom:1px dotted #bbb}
.date{width:27px;height:29px;background:#444;color:#fff;text-align:center;font-size:11px;line-height:13px;padding-top:2px;flex:none}
.date small{display:block;font-size:7px;line-height:10px;border-top:1px solid #777}
.item-title{font-size:9.5px;font-weight:700;color:var(--dark)}
.item-text{font-size:8.5px;line-height:13px;color:#555}
.more{position:absolute;font-size:9px;font-weight:700;color:var(--blue)}
.do-item{position:absolute;left:10px;width:192px;padding-left:20px}
.do-item .tick{position:absolute;left:0;top:2px}
.do-item .item-title{font-size:10.5px;font-weight:700;margin-bottom:1px}
.divider{position:absolute;left:12px;width:190px;border-top:1px dashed #ccc}
.avatar{position:absolute;left:11px;top:50px;width:64px;height:64px;border-radius:50%;border:2px solid var(--blue);background:radial-gradient(circle at 50% 40%,#c9a58c,#6a5548 60%,#dfe8ee 61%)}
.person{position:absolute;left:86px;top:69px;font-size:11px;color:var(--dark)}
.person small{display:block;font-size:8.5px;color:#555;margin-top:3px}
.quote{position:absolute;left:10px;top:131px;width:192px;height:76px;border:1px solid #e4e4e4;padding:6px 9px;font-size:9.5px;line-height:15.5px;font-style:italic;color:#444}
.quote .mark{color:#ccc;font-size:12px;line-height:1}
.quote-tail{position:absolute;left:60px;top:-7px;width:12px;height:12px;background:#fff;border-left:1px solid #e4e4e4;border-top:1px solid #e4e4e4;transform:rotate(45deg)}
.dots{position:absolute;right:10px;bottom:8px;display:flex;gap:5px}
.dots i{width:5px;height:5px;border-radius:50%;background:#ccc}
.dots i.on{background:var(--red)}
.band{left:0;top:893px;width:882px;height:200px;background:var(--grey-band)}
.ribbon{left:352px;top:893px}
.ribbon-label{left:352px;top:897px;width:178px;text-align:center;font-family:"Roboto",sans-serif;font-weight:500;font-size:14.5px;color:#fff}
.tile{top:946px;width:166px;height:118px;border:2px solid #fff;box-shadow:0 1px 3px rgba(0,0,0,.15);overflow:hidden}
.tile .photo{width:100%;height:100%}
.tile .caption{position:absolute;left:0;bottom:0;width:100%;height:22px;background:rgba(26,170,220,.88);color:#fff;text-align:center;font-size:12px;line-height:22px;font-weight:700}
.arrow{top:995px}
.footer{left:0;top:1093px;width:882px;height:103px;background:var(--footer)}
.footer-brand{left:0;top:1110px;width:882px;display:flex;justify-content:center;align-items:center;gap:7px;font-size:19px;font-weight:700;color:var(--blue)}
.footer-nav{left:0;top:1152px;width:882px;display:flex;justify-content:center;list-style:none}
.footer-nav li{font-size:9px;color:#fff;font-weight:700;padding:0 8px;border-left:1px solid #555;line-height:11px}
.footer-nav li:first-child{border-left:0;color:var(--blue);font-weight:400}
.copyright{left:0;top:1177px;width:882px;text-align:center;font-size:8.5px;color:#bbb}
.bottom-bar{left:0;top:1196px;width:882px;height:4px;background:var(--blue)}
</style>
</head>
<body>
<div class="abs top-bar"></div>

<header>
  <div class="abs brand"><span class="brand-dot"></span>Brenwick Structures</div>
  <div class="abs call"><em>Call us TODAY !</em>
    <span class="phone">
      <svg width="13" height="13" viewBox="0 0 24 24"><path fill="#1a9ad6" d="M6.6 10.8a15 15 0 0 0 6.6 6.6l2.2-2.2c.3-.3.7-.4 1-.2 1.1.4 2.3.6 3.6.6.6 0 1 .4 1 1V20c0 .6-.4 1-1 1A17 17 0 0 1 3 4c0-.6.4-1 1-1h3.5c.6 0 1 .4 1 1 0 1.3.2 2.5.6 3.6.1.3 0 .7-.2 1z"/></svg>
      +555 018 2744</span>
  </div>
  <nav class="abs nav">
    <ul>
      <li class="active">HOME</li><li>PORTFOLIO</li><li>PRODUCT SPECS</li><li>TESTIMONIALS</li><li>OUR PROCESS</li><li>CONTACT US</li>
    </ul>
  </nav>
</header>

<section>
  <svg class="abs hero" width="882" height="340" viewBox="0 0 882 340">
    <defs>
      <linearGradient id="sky" x1="0" y1="0" x2="0" y2="1">
        <stop offset="0" stop-color="#1b3f6e"/>
        <stop offset=".45" stop-color="#4f9ad6"/>
        <stop offset=".75" stop-color="#2d6aa6"/>
        <stop offset="1" stop-color="#16325a"/>
      </linearGradient>
    </defs>
    <path role="img" aria-label="Glass office towers seen from below against a blue sky" fill="url(#sky)" d="M0 0H882V280Q441 368 0 280Z"/>
    <path d="M0 288Q441 376 882 288" fill="none" stroke="#d9261c" stroke-width="4"/>
    <circle cx="420" cy="308" r="3.5" fill="#d9261c"/>
    <circle cx="434" cy="308" r="3.5" fill="#aac"/>
    <circle cx="448" cy="308" r="3.5" fill="#aac"/>
    <circle cx="462" cy="308" r="3.5" fill="#aac"/>
  </svg>
  <h1 class="abs hero-title" style="font-weight:400">Building Dreams, So You Can Build Memories</h1>
</section>

<section>
  <h2 class="abs welcome" style="font-weight:400">WELCOME TO <span>BRENWICK STRUCTURES</span></h2>
  <p class="abs intro">Lorem ipsum dolor sit amet, consectetur adipiscing elit. Praesent volutpat ultricies euismod. Mauris consectetur tellus quis sem dictum pharetra. Nullam euismod nunc blandit mi sagittis, et posuere nunc iaculis. Aenean in sollicitudin quam, non accumsan ipsum. Vivamus in aliquet ex. Nullam malesuadammodo mi, tristique faucibus nisl condimentum condimentum. Duis porttitor nisi ut elementum so</p>
  <div class="abs read-more">READ MORE</div>
</section>

<section>
  <article class="abs card" style="left:96px">
    <div class="card-head"><span class="icon"><svg width="14" height="12" viewBox="0 0 14 12"><path fill="#fff" d="M1 4h3l6-3v10L4 8H1zM4 8l1 4h2L6 8z"/></svg></span>LATEST NEWS</div>
    <div class="news-item" style="top:47px"><div class="date">22<small>JULY</small></div><div><div class="item-title">Vero eros accumsaet odio</div><div class="item-text">quis nostrud exetiperj suscipit lobtis nisl ut aliquip ex ea commod</div></div></div>
    <div class="news-item" style="top:100px"><div class="date">22<small>JULY</small></div><div><div class="item-title">Eros accumsaet iusto odio</div><div class="item-text">quis nostrud exetiperj suscipit lobtfis nisl ut aliquip exea commod</div></div></div>
    <div class="news-item" style="top:154px;border-bottom:0"><div class="date">22<small>JULY</small></div><div><div class="item-title">Croeros accumsaet iusto odio</div><div class="item-text">quis nostrud exetiperj suscipit lobtisf nisl ut aliquip ex commod</div></div></div>
    <div class="more" style="left:137px;top:202px">READ MORE
      <svg width="9" height="9" viewBox="0 0 10 10" style="vertical-align:-1px"><circle cx="5" cy="5" r="5" fill="#555"/><path d="M5 2.5v5M2.5 5h5" stroke="#fff" stroke-width="1.4"/></svg></div>
  </article>

  <article class="abs card" style="left:334px">
    <div class="card-head"><span class="icon"><svg width="13" height="13" viewBox="0 0 14 14"><rect x="1.5" y="2.5" width="11" height="10" fill="none" stroke="#fff" stroke-width="1.3"/><path d="M1.5 5.5h11M4 1v3M10 1v3" stroke="#fff" stroke-width="1.3"/></svg></span>WHAT WE DO</div>
    <div class="do-item" style="top:49px"><svg class="tick" width="11" height="9" viewBox="0 0 11 9"><path d="M1 4.5l3 3 6-6" fill="none" stroke="#4a8a8f" stroke-width="2"/></svg>
      <div class="item-title">Vulputate Molestie Consequat</div><div class="item-text">quis nostrud exsetiperj&nbsp; aliquip commod consequa uisquis nostru suscipit nisl roli aliquip exea commod</div></div>
    <div class="more" style="right:6px;top:106px">KNOW MORE</div>
    <div class="divider" style="top:124px"></div>
    <div class="do-item" style="top:133px"><svg class="tick" width="11" height="9" viewBox="0 0 11 9"><path d="M1 4.5l3 3 6-6" fill="none" stroke="#4a8a8f" stroke-width="2"/></svg>
      <div class="item-title">Vulputate Molestie Consequat</div><div class="item-text">quis nostrud exetiperj saliquip commodr consequa uisquis nostru iexetip suscipitt lobtis nisl ut aliquip exea commod</div></div>
    <div class="more" style="right:6px;top:202px">KNOW MORE</div>
  </article>

  <article class="abs card" style="left:572px">
    <div class="card-head"><span class="icon"><svg width="14" height="13" viewBox="0 0 14 13"><ellipse cx="7" cy="5.5" rx="5.5" ry="4.3" fill="none" stroke="#fff" stroke-width="1.3"/><path d="M3.5 8.5L2.5 12l3.5-2.5" fill="#fff"/></svg></span>TESTIMONIALS</div>
    <div class="avatar" role="img" aria-label="Portrait photo of the client giving the testimonial"></div>
    <div class="person">Marlo Venner<small>Bussiness Man</small></div>
    <div class="quote"><span class="quote-tail"></span><span class="mark">“</span> Ut wisi enim ad minim veniam, quism nostrli erci tation ullamcorper suscipitop lobortis commodo <span class="mark">”</span><br>consequat.
      <div class="dots"><i></i><i class="on"></i><i></i><i></i></div></div>
  </article>
</section>

<section>
  <div class="abs band"></div>
  <svg class="abs ribbon" width="178" height="25" viewBox="0 0 178 25"><path d="M0 0H178L168 25H10Z" fill="#d9261c"/></svg>
  <h2 class="abs ribbon-label">BUILDING TYPES</h2>
  <svg class="abs arrow" width="10" height="16" viewBox="0 0 10 16" style="left:78px"><path d="M8 1L2 8l6 7" fill="none" stroke="#aaa" stroke-width="2"/></svg>
  <svg class="abs arrow" width="10" height="16" viewBox="0 0 10 16" style="left:794px"><path d="M2 1l6 7-6 7" fill="none" stroke="#888" stroke-width="2"/></svg>
  <figure class="abs tile" style="left:97px"><div class="photo" role="img" aria-label="Farm shop buildings under an overcast sky" style="background:linear-gradient(#c9cfd2 0,#dcdcd6 45%,#8c7766 70%,#6e7d57 100%)"></div><figcaption class="caption">Farm Shops</figcaption></figure>
  <figure class="abs tile" style="left:271px"><div class="photo" role="img" aria-label="Open machine storage shed with equipment" style="background:linear-gradient(#9ec4e2 0,#c6d9e6 35%,#6f7a82 60%,#8a8560 100%)"></div><figcaption class="caption">Machine Storage</figcaption></figure>
  <figure class="abs tile" style="left:445px"><div class="photo" role="img" aria-label="Seed dealership building with silos and a truck" style="background:linear-gradient(#b9cde0 0,#d9dfe2 40%,#cfd4c8 65%,#7d8c6a 100%)"></div><figcaption class="caption">Seed Dealership</figcaption></figure>
  <figure class="abs tile" style="left:618px"><div class="photo" role="img" aria-label="Aerial view of a long dairy barn in green fields" style="background:linear-gradient(#6f9a4c 0,#9aa27a 40%,#c9a86a 65%,#5f8a3e 100%)"></div><figcaption class="caption">Dairy</figcaption></figure>
</section>

<footer>
  <div class="abs footer"></div>
  <div class="abs footer-brand"><span class="brand-dot" style="width:11px;height:11px;background:var(--red)"></span>Brenwick Structures</div>
  <ul class="abs footer-nav">
    <li>HOME</li><li>PORTFOLIO</li><li>PRODUCT SPACS</li><li>TESTIMONIALS</li><li>OUR PROCESS</li><li>CONTACT US</li>
  </ul>
  <p class="abs copyright">Copyright © 2015 Brenwick Structures&nbsp; | All Rights Reserved</p>
  <div class="abs bottom-bar"></div>
</footer>
</body>
</html>
```